Business card for Property Management consultant

I need a business card for my business LX Vantage - I consult to real estate agents to improve the performance of their Property Management departments (rental houses management). The card needs to be very professional looking, incorporating our logo and my photo plus the line "Grow your Rent Roll with Purpose"

Target Market(s)

Real Estate business owners

Industry/Entity Type

Business Consultant

Contact Information for Business Card

Business name - LX Vantage (logo uploaded)
My Name : Marcia Kellaway -
Title : Property Management Consultant

Grow your Rent Roll with Purpose

Phone : +61 438592716
email : marcia@lxvantage.com.au
website ; www.lxvantage.com.au

Requirements
Must have
• Logo
• My photo
• Very corporate / professional look

```html
<!DOCTYPE html>
<html lang="en">
<head>
<meta charset="utf-8">
<title>LX Vantage – Business Card</title>
<link href="https://fonts.googleapis.com/css2?family=Open+Sans:wght@400;600;700&display=swap" rel="stylesheet">
<style>
  :root {
    --page-bg: #e9e9eb;
    --card-bg: #ffffff;
    --ink: #2b2b33;
    --ink-soft: #3a3a40;
    --brand-blue: #234f9e;
    --accent-blue: #2f6fd0;
    --rule: #4a4a4f;
    --band-black: #151515;
    --band-grey: #c9c9cc;
    --band-grey-text: #3c3c40;
    --white: #ffffff;
  }
  * { margin: 0; padding: 0; box-sizing: border-box; }
  html, body {
    width: 1200px; height: 867px; overflow: hidden;
    background: var(--page-bg);
    font-family: "Open Sans", Arial, sans-serif;
  }
  .card {
    position: absolute; left: 150px; top: 158px;
    width: 900px; height: 550px;
    background: var(--card-bg);
    box-shadow: 0 6px 24px rgba(0,0,0,.18);
    overflow: hidden;
  }
  .brand {
    position: absolute; left: 56px; top: 82px;
    display: flex; align-items: center; gap: 16px;
  }
  .brand-mark { width: 44px; height: 44px; background: var(--accent-blue); }
  .brand-name {
    font-size: 58px; font-weight: 600; color: var(--ink);
    letter-spacing: 1px; line-height: 1;
  }
  .brand-rule {
    position: absolute; left: 56px; top: 162px;
    width: 400px; height: 2px; background: var(--accent-blue);
  }
  .brand-tagline {
    position: absolute; left: 56px; top: 170px;
    font-size: 22px; font-weight: 400; color: var(--ink-soft);
    letter-spacing: 3px; white-space: nowrap;
  }
  .divider {
    position: absolute; left: 56px; top: 236px;
    width: 470px; height: 1px; background: var(--rule);
  }
  .person { position: absolute; left: 112px; top: 262px; }
  .person-name { font-size: 27px; font-weight: 600; color: var(--brand-blue); }
  .person-title { font-size: 20px; color: var(--ink-soft); margin-top: 2px; }
  .person-rule {
    position: absolute; left: 112px; top: 342px;
    width: 190px; height: 1px; background: var(--rule);
  }
  .contact {
    position: absolute; left: 112px; top: 360px;
    font-size: 19px; color: var(--ink-soft); line-height: 30px;
  }
  .photo {
    position: absolute; right: 0; top: 0;
    width: 340px; height: 440px;
    background: linear-gradient(180deg, #f4f4f6 0%, #e6dcd6 35%, #3f72d6 70%, #1f4fb8 100%);
  }
  .band-grey {
    position: absolute; left: 0; top: 440px;
    width: 900px; height: 34px; background: var(--band-grey);
  }
  .web {
    position: absolute; right: 30px; top: 444px;
    display: flex; align-items: center; gap: 12px;
    font-size: 18px; color: var(--band-grey-text); white-space: nowrap;
  }
  .web-mark { width: 18px; height: 18px; background: var(--accent-blue); }
  .band-black {
    position: absolute; left: 0; top: 474px;
    width: 900px; height: 56px; background: var(--band-black);
  }
  .slogan {
    position: absolute; left: 112px; top: 486px;
    font-size: 24px; font-weight: 700; color: var(--white); white-space: nowrap;
  }
</style>
</head>
<body>
  <div class="card">
    <div class="brand">
      <div class="brand-mark"></div>
      <div class="brand-name">LX Vantage</div>
    </div>
    <div class="brand-rule"></div>
    <div class="brand-tagline">PLAN - BUILD - PROSPER</div>
    <div class="divider"></div>

    <div class="person">
      <div class="person-name">Marcia Kellaway</div>
      <div class="person-title">Property Management Consultant</div>
    </div>
    <div class="person-rule"></div>

    <div class="contact">
      <div>Phone: +61 438592716</div>
      <div>Email: marcia@lxvantage.com.au</div>
    </div>

    <div class="photo" role="img" aria-label="Portrait photo of Marcia Kellaway in a blue jacket"></div>

    <div class="band-grey"></div>
    <div class="web">
      <div class="web-mark"></div>
      <span>www.lxvantage.com.au</span>
    </div>
    <div class="band-black"></div>
    <div class="slogan">Grow your Rent Roll with Purpose</div>
  </div>
</body>
</html>
```